HIGH-END ANTI AGING START-UP NEEDS DOCUMENT/LETTERHEAD DESIGN!!!!

We are a high end anti-aging and health start-up catering to clients in Stamford and NYC. We just did a logo redesign and are now looking for a letter head design that we can use IN GOOGLE DOCS for marrowfieldcaregroup.example clients. We are REALLY EXCITED to see what you can show us!!!!!!!! We need something sophisticated and MODERN! Thanks so much!

Target Market(s)

High end, boutique medical clients. Our clientele is fairly high profile and we need a sleek, sophisticated letter head to put on all of our marketing materials and medical forms as well.

Industry/Entity Type

Medical

Font styles to use
Serif
Sans Serif

Colors
0255a3
ffffff
00a990
1b1b1b
919191

Requirements
Must have
• Must have the logo and "Marrowfield Care Group" written somewhere. Must have our URL www.marrowfieldcaregroup.example.
Nice to have
• office phone number (555) 374-9102
Should not have
• Colors outside of our logo colors + grey + black

```html
<!DOCTYPE html>
<html lang="en">
<head>
<meta charset="utf-8">
<title>Marrowfield Care Group — Letterhead</title>
<link href="https://fonts.googleapis.com/css2?family=Open+Sans:wght@400;600;700&display=swap" rel="stylesheet">
<style>
  :root {
    --backdrop: #8a7f72;
    --paper: #ffffff;
    --brand-blue: #4a70b8;
    --brand-green: #1e8a45;
    --ink: #1b1b1b;
    --mark-tint: #e6ede2;
    --mark-tint-blue: #e4e7f3;
  }
  * { box-sizing: border-box; margin: 0; padding: 0; }
  html, body {
    width: 1200px; height: 795px; overflow: hidden;
    background: var(--backdrop);
    font-family: "Open Sans", Arial, sans-serif;
  }
  .letterhead {
    position: absolute;
    left: 335px; top: 40px;
    width: 530px; height: 715px;
    background: var(--paper);
    box-shadow: 0 6px 18px rgba(0,0,0,0.25);
    overflow: hidden;
  }
  .brand {
    position: absolute; left: 150px; top: 52px;
    display: flex; align-items: center; gap: 8px;
  }
  .brand-dot {
    width: 26px; height: 26px; border-radius: 50%;
    background: var(--brand-green);
  }
  .brand-name {
    font-weight: 700; font-size: 15px; color: var(--brand-blue);
  }
  .backdrop-mark {
    position: absolute; left: 95px; top: 170px;
    width: 330px; height: 330px; border-radius: 50%;
    background: var(--mark-tint);
  }
  .contact {
    position: absolute; right: 30px; bottom: 78px;
    text-align: right; color: var(--ink);
    font-size: 11.5px; line-height: 1.45;
  }
  .contact-name { font-weight: 700; color: var(--brand-blue); }
  .contact-line { display: flex; justify-content: flex-end; align-items: center; gap: 4px; }
  .contact-icon { width: 12px; height: 12px; flex: none; }
  .footer-band {
    position: absolute; left: 0; right: 0; bottom: 14px;
    height: 44px;
    background: var(--brand-blue);
    border-top: 3px solid var(--brand-green);
    border-bottom: 3px solid var(--brand-green);
    box-shadow: inset 0 2px 0 var(--paper), inset 0 -2px 0 var(--paper);
  }
  .footer-url {
    position: absolute; right: 110px; top: 10px;
    color: var(--paper); font-size: 13px; letter-spacing: 0.8px;
  }
  .footer-dot {
    position: absolute; right: 14px; top: -22px;
    width: 34px; height: 34px; border-radius: 50%;
    background: var(--brand-green);
    border: 3px solid var(--paper);
  }
</style>
</head>
<body>
  <main class="letterhead">
    <header class="brand">
      <span class="brand-dot"></span>
      <span class="brand-name">Marrowfield Care Group</span>
    </header>

    <div class="backdrop-mark" aria-hidden="true"></div>

    <address class="contact" style="font-style:normal">
      <div class="contact-name">Marrowfield Care Group</div>
      <div>18 Linden Ave. Suite 410, Fairhaven CT, 06999</div>
      <div class="contact-line">
        <svg class="contact-icon" viewBox="0 0 12 12" aria-hidden="true">
          <circle cx="6" cy="6" r="6" fill="var(--brand-blue)"/>
          <path d="M4 3 L5 3 L5.6 4.6 L4.9 5.2 Q5.6 6.6 6.8 7.1 L7.4 6.4 L9 7 L9 8 Q8.5 9 7.5 8.8 Q4.2 8 3.2 4.5 Q3.1 3.4 4 3 Z" fill="#fff"/>
        </svg>
        <span>(555) 374-9102</span>
        <svg class="contact-icon" viewBox="0 0 12 12" aria-hidden="true">
          <circle cx="6" cy="6" r="6" fill="var(--brand-blue)"/>
          <rect x="3" y="4" width="6" height="4.2" fill="#fff"/>
          <path d="M3 4 L6 6.4 L9 4" stroke="var(--brand-blue)" stroke-width="0.7" fill="none"/>
        </svg>
        <span>info@marrowfieldcaregroup.example</span>
      </div>
    </address>

    <footer class="footer-band">
      <span class="footer-url">www.marrowfieldcaregroup.example</span>
      <span class="footer-dot"></span>
    </footer>
  </main>
</body>
</html>
```